全国の1人〜2人で営業されている理・美容室のオーナーさん方にコロナでも全く影響を受けてない当サロンのノウハウを読んで頂きたいと思っています。
これからのサロンのあり方、考え方、今すぐに取り入れるべき技術や商品、売り上げの上げ方などをお伝えします。本気で環境を変えたい方、美容師の仕事、接客、人をキレイにすることが大好きな方、意識の高いお客様に囲まれずっと通って頂けるような、そんな美容室を一緒に作って行きたいです。

この度はご提案、修正と本当にありがとうございました。最後の最後までかなり悩みました。
初めての電子書籍で良い表紙デザインと出会うことが出来ました。

今回、ご提案頂いた皆さん、本当にありがとうございました。初心者の自分に親身になって頂き、皆さんの丁寧なデザインに感動しました。また2冊目も考えています。ご縁があればまたよろしくお願いします。

```html
<!DOCTYPE html>
<html lang="ja">
<head>
<meta charset="UTF-8">
<title>これからサロンが生き残る方法</title>
<link href="https://fonts.googleapis.com/css2?family=M+PLUS+Rounded+1c:wght@700;800;900&display=swap" rel="stylesheet">
<style>
  :root {
    --cover-red: #b3102c;
    --ink-white: #ffffff;
    --figure-tone-1: #c98a5a;
    --figure-tone-2: #7fa0c4;
  }
  html, body {
    margin: 0;
    padding: 0;
    width: 750px;
    height: 1200px;
    overflow: hidden;
    background: var(--cover-red);
  }
  .cover {
    position: relative;
    width: 750px;
    height: 1200px;
    background: var(--cover-red);
    color: var(--ink-white);
    font-family: "M PLUS Rounded 1c", sans-serif;
    font-weight: 800;
    overflow: hidden;
  }
  .tagline {
    position: absolute;
    left: 20px;
    top: 16px;
    margin: 0;
    font-size: 48px;
    font-weight: 800;
    line-height: 1;
    letter-spacing: 0;
    white-space: nowrap;
  }
  .title {
    margin: 0;
    font-weight: 900;
  }
  .title span {
    position: absolute;
    left: 70px;
    line-height: 1;
    white-space: nowrap;
  }
  .title .line-1 { top: 150px; font-size: 112px; letter-spacing: 2px; }
  .title .line-2 { top: 272px; font-size: 158px; letter-spacing: 0; }
  .title .line-3 { top: 455px; font-size: 146px; letter-spacing: 2px; }
  .title .line-4 { top: 660px; font-size: 166px; letter-spacing: 4px; }
  .stylist-figure {
    position: absolute;
    left: 505px;
    top: 625px;
    width: 175px;
    height: 545px;
    border-radius: 88px 88px 20px 20px;
    background: linear-gradient(180deg, var(--figure-tone-1) 0%, var(--figure-tone-1) 45%, var(--figure-tone-2) 100%);
    opacity: 0.85;
  }
  .author {
    position: absolute;
    left: 70px;
    top: 985px;
    font-weight: 800;
  }
  .author .label { font-size: 42px; line-height: 1; display: block; }
  .author .name { font-size: 56px; line-height: 1; display: block; margin-top: 36px; letter-spacing: 2px; white-space: nowrap; }
</style>
</head>
<body>
  <main class="cover">
    <p class="tagline">コロナや景気に左右されない、</p>
    <h1 class="title">
      <span class="line-1">これから</span>
      <span class="line-2">サロンが</span>
      <span class="line-3">生き残る</span>
      <span class="line-4">方法</span>
    </h1>
    <div class="stylist-figure" role="img" aria-label="Illustration of a female hairstylist holding scissors, wearing a tool belt"></div>
    <div class="author">
      <span class="label">著者</span>
      <span class="name">たかはしみさき</span>
    </div>
  </main>
</body>
</html>
```